Quorvex clinic business card - double sided for young clinic

I require business cards for my aesthetic clinic specialising in the below treatments. I would like the cards to be modern as my clinic base are young 22-35 years old. I require my logo on it and would like the edges to be rounded.

I have an aesthetic clinic specialising in :
Quorvex
Lip Enhancement
Chemical Peels
Facial Fillers
Non Surgical Face Lift

I would the cards to have the following information on them:
My logo - (in grey/silver)
address
Phone number
services

Colours :
White/grey/silver and red

a nice image on there, perhaps a set of lips as this is a main service i deliver

Company Name: PDA Address: 52 Farrowmere Road, 4 Brackwell High Street, KT9 4WQ Phone: 0208 794 2160 Website: www.penningtondoweaesthetics.co.uk

Target Market(s)

clinics 22-45 years old mainly female

Industry/Entity Type

Business

Contact Information for Business Card

as above

Requirements
Must have
• logo
• Address
• Email
• Phone number
• Services i offer
Nice to have
• images

```html
<!DOCTYPE html>
<html lang="en">
<head>
<meta charset="utf-8">
<title>Pennington Dowe Aesthetics – Business Card</title>
<link rel="stylesheet" href="https://fonts.googleapis.com/css2?family=Gentium+Book+Plus&display=swap">
<style>
  :root {
    --page: #ececec;
    --card-dark: #1c1c1c;
    --silver: #a9a9a9;
    --ink: #2b2b2b;
    --paper: #ffffff;
    --contact-text: #e6e6e6;
    --icon-bg: #6e6e6e;
    --icon-ink: #2a2a2a;
  }
  * { margin: 0; padding: 0; box-sizing: border-box; }
  html, body { width: 1200px; height: 1200px; overflow: hidden; }
  body {
    background: var(--page);
    font-family: "Gentium Book Plus", Georgia, serif;
    position: relative;
  }
  .card {
    position: absolute;
    left: 210px;
    width: 780px;
    height: 443px;
    overflow: hidden;
    box-shadow: 0 6px 14px rgba(0,0,0,0.18);
  }
  .card--front { top: 150px; background: var(--card-dark); }
  .card--back { top: 661px; background: var(--paper); }

  .facets { position: absolute; left: 0; top: 0; width: 780px; height: 443px; }

  .brand-mark {
    position: absolute;
    left: 0; right: 0; top: 160px;
    text-align: center;
    color: var(--silver);
    font-size: 42px;
    letter-spacing: 4px;
    line-height: 1;
  }
  .front-name, .back-name {
    position: absolute;
    left: 0; right: 0;
    text-align: center;
    text-transform: uppercase;
    line-height: 1;
    white-space: nowrap;
  }
  .front-name { top: 276px; color: var(--silver); }
  .front-name__line1 { display: block; font-size: 28px; letter-spacing: 4px; }
  .front-name__line2 { display: block; font-size: 46px; letter-spacing: 5px; margin-top: 2px; }

  .back-name { top: 62px; color: var(--ink); }
  .back-name__line1 { display: block; font-size: 46px; letter-spacing: 6px; }
  .back-name__line2 { display: block; font-size: 70px; letter-spacing: 9px; margin-top: 2px; }

  .contact-band { position: absolute; left: 0; top: 0; width: 780px; height: 443px; }

  .contact {
    position: absolute;
    display: flex;
    align-items: center;
    color: var(--contact-text);
    font-size: 21px;
    line-height: 1.3;
    white-space: nowrap;
  }
  .contact__icon {
    width: 48px; height: 48px;
    border-radius: 50%;
    background: var(--icon-bg);
    display: flex; align-items: center; justify-content: center;
    flex: 0 0 48px;
    margin-right: 18px;
  }
  .contact__icon svg { width: 24px; height: 24px; fill: var(--icon-ink); }
  .contact--address { left: 40px; top: 258px; }
  .contact--phone   { left: 40px; top: 350px; }
  .contact--email   { left: 356px; top: 262px; }
  .contact--web     { left: 356px; top: 346px; }
</style>
</head>
<body>

<section class="card card--front">
  <svg class="facets" viewBox="0 0 780 443" role="img" aria-label="Dark faceted low-poly background in charcoal and black tones">
    <rect width="780" height="443" fill="#1d1d1d"/>
    <polygon points="0,0 300,0 290,55 0,90" fill="#2b2b2b"/>
    <polygon points="290,55 300,0 460,0 440,110" fill="#141414"/>
    <polygon points="460,0 780,0 780,120 640,110" fill="#262626"/>
    <polygon points="0,90 290,55 200,230 0,260" fill="#242424"/>
    <polygon points="640,110 780,120 780,300 500,330" fill="#181818"/>
    <polygon points="500,330 640,70 720,380" fill="#303030"/>
    <polygon points="0,330 190,350 150,443 0,443" fill="#111111"/>
    <polygon points="190,350 500,330 560,443 150,443" fill="#1a1a1a"/>
    <polygon points="720,380 780,330 780,443 640,443" fill="#4a4a4a"/>
  </svg>
  <div class="brand-mark">PDA</div>
  <div class="front-name">
    <span class="front-name__line1">Pennington Dowe</span>
    <span class="front-name__line2">Aesthetics</span>
  </div>
</section>

<section class="card card--back">
  <div class="back-name">
    <span class="back-name__line1">Pennington Dowe</span>
    <span class="back-name__line2">Aesthetics</span>
  </div>

  <svg class="contact-band" viewBox="0 0 780 443" role="img" aria-label="Dark faceted band holding the contact details">
    <defs>
      <linearGradient id="sheen" x1="0" y1="0" x2="1" y2="0">
        <stop offset="0" stop-color="#ffffff" stop-opacity="0"/>
        <stop offset="1" stop-color="#bdbdbd"/>
      </linearGradient>
    </defs>
    <polygon points="0,225 780,208 780,443 0,443" fill="url(#sheen)"/>
    <polygon points="0,226 280,222 780,246 780,443 0,443" fill="#242424"/>
    <polygon points="0,226 280,222 250,443 0,443" fill="#333333"/>
    <polygon points="280,222 780,246 780,330 420,300" fill="#1a1a1a"/>
    <polygon points="250,443 280,222 420,300 470,443" fill="#2c2c2c"/>
    <polygon points="470,443 420,300 780,330 780,443" fill="#141414"/>
  </svg>

  <div class="contact contact--address">
    <span class="contact__icon"><svg viewBox="0 0 24 24"><path d="M12 3 2 12h3v8h5v-5h4v5h5v-8h3z"/></svg></span>
    <span>52 Farrowmere Road,<br>Brackwell, KT9 4WQ</span>
  </div>
  <div class="contact contact--phone">
    <span class="contact__icon"><svg viewBox="0 0 24 24"><path d="M6.6 10.8a15.1 15.1 0 0 0 6.6 6.6l2.2-2.2c.3-.3.7-.4 1-.2 1.1.4 2.3.6 3.6.6.6 0 1 .4 1 1V20c0 .6-.4 1-1 1A17 17 0 0 1 3 4c0-.6.4-1 1-1h3.5c.6 0 1 .4 1 1 0 1.3.2 2.5.6 3.6.1.3 0 .7-.2 1z"/></svg></span>
    <span>020 8794 2160</span>
  </div>
  <div class="contact contact--email">
    <span class="contact__icon"><svg viewBox="0 0 24 24"><path d="M3 6h18v12H3zm1.5 1.5v.3L12 13l7.5-5.2v-.3zm0 2.1v6.9h15V9.6L12 14.8z"/></svg></span>
    <span>pdabrackwellbookings@mailbox.com</span>
  </div>
  <div class="contact contact--web">
    <span class="contact__icon"><svg viewBox="0 0 24 24"><path d="M12 2a10 10 0 1 0 0 20 10 10 0 0 0 0-20zm0 2c.8 1.2 1.5 2.5 1.9 4h-3.8c.4-1.5 1.1-2.8 1.9-4zM4.3 14a8 8 0 0 1 0-4h3.4a16 16 0 0 0 0 4zm5.4 0a14 14 0 0 1 0-4h4.6a14 14 0 0 1 0 4zm6.6 0a16 16 0 0 0 0-4h3.4a8 8 0 0 1 0 4zM12 20c-.8-1.2-1.5-2.5-1.9-4h3.8c-.4 1.5-1.1 2.8-1.9 4z"/></svg></span>
    <span>www.penningtondoweaesthetics.co.uk</span>
  </div>
</section>

</body>
</html>
```